Design a Flyer

I need an eye-catching flyer designed which showcases some key benefits on my product and entices the viewer to purchase. The target market would be university students, and I would like for an image of an owl to be used somewhere on the flyer.
I may also like to use a discount code for 5% off, though im not certain at the moment.
Details of the product can be found at velostrix.com though the current pictures f the product on the website are only place holder images. I should have the actual images soon
Target Market(s)
university students
Industry/Entity Type
University
Look and feel

```html
<!DOCTYPE html>
<html lang="en">
<head>
<meta charset="utf-8">
<title>Velostrix Brain Booster Flyer</title>
<link rel="stylesheet" href="https://fonts.googleapis.com/css2?family=Open+Sans:wght@300;400;600&display=swap">
<style>
  :root {
    --teal: #3cc4c4;
    --grey-band: #6e6e70;
    --grey-text: #8a8a8a;
    --body-text: #4a4a4a;
    --brand-grey: #6b6b6b;
    --paper: #ffffff;
    --owl-mid: #8a7560;
    --owl-light: #d9d0c4;
  }
  * { margin: 0; padding: 0; box-sizing: border-box; }
  html, body { width: 868px; height: 1200px; overflow: hidden; background: #f2f2f2; }
  body { font-family: "Open Sans", Arial, sans-serif; color: var(--body-text); }

  .flyer {
    position: relative;
    width: 868px;
    height: 1200px;
    background: var(--paper);
    overflow: hidden;
  }
  .edge-band { position: absolute; left: 0; width: 868px; height: 20px; }
  .edge-band--top { top: 0; }
  .edge-band--bottom { bottom: 0; }

  .discount {
    position: absolute;
    top: 106px;
    left: 92px;
    display: flex;
    align-items: center;
    gap: 14px;
  }
  .discount__label {
    text-align: right;
    font-size: 18px;
    line-height: 27px;
    font-weight: 400;
    color: var(--grey-text);
  }
  .discount__amount {
    font-size: 56px;
    font-weight: 300;
    color: var(--teal);
    line-height: 1;
  }
  .discount__amount small { font-size: 30px; }

  .brand {
    position: absolute;
    top: 178px;
    left: 500px;
    width: 300px;
    text-align: center;
  }
  .brand__name {
    font-size: 36px;
    font-weight: 400;
    letter-spacing: 2px;
    color: var(--brand-grey);
    line-height: 1;
  }
  .brand__tagline {
    margin-top: 14px;
    font-size: 18px;
    font-weight: 400;
    color: var(--brand-grey);
    letter-spacing: 1px;
  }

  .intro {
    position: absolute;
    top: 240px;
    left: 92px;
    width: 686px;
  }
  .section-title {
    font-size: 27px;
    font-weight: 400;
    color: var(--teal);
    line-height: 1.3;
  }
  .intro p {
    margin-top: 14px;
    font-size: 15.5px;
    line-height: 23px;
    text-align: justify;
  }
  .intro p + p { margin-top: 22px; }

  .benefits {
    position: absolute;
    top: 548px;
    left: 92px;
    width: 420px;
  }
  .benefit-list { list-style: none; margin-top: 18px; }
  .benefit-list li {
    display: flex;
    align-items: center;
    gap: 10px;
    font-size: 18px;
    line-height: 27px;
    color: var(--grey-text);
  }
  .benefit-list svg { width: 18px; height: 18px; flex: none; }

  .guarantee-seal {
    position: absolute;
    top: 626px;
    left: 328px;
    width: 156px;
    height: 156px;
  }

  .product-photo {
    position: absolute;
    top: 548px;
    left: 503px;
    width: 286px;
    height: 258px;
    border-radius: 30px 30px 0 0;
    background: linear-gradient(180deg, #eceff0 0%, #f7f8f8 38%, var(--teal) 39%, var(--teal) 62%, #f3f5f5 63%, #ffffff 100%);
  }

  .owl-photo {
    position: absolute;
    top: 812px;
    left: 88px;
    width: 692px;
    height: 368px;
    background: radial-gradient(ellipse 55% 60% at 50% 45%, var(--owl-mid) 0%, var(--owl-light) 55%, rgba(255,255,255,0) 100%);
  }

  .contact {
    position: absolute;
    top: 1098px;
    font-style: normal;
    font-size: 17.5px;
    line-height: 24px;
    color: var(--body-text);
  }
  .contact--address { left: 94px; }
  .contact--online { left: 543px; }
  .contact__row { display: flex; align-items: flex-start; gap: 6px; }
  .contact__row svg { width: 15px; height: 15px; margin-top: 5px; flex: none; }
  .contact__indent { padding-left: 21px; }
</style>
</head>
<body>
<main class="flyer">
  <svg class="edge-band edge-band--top" viewBox="0 0 868 20" preserveAspectRatio="none">
    <polygon points="0,0 98,0 86,20 0,20" fill="var(--teal)"/>
    <polygon points="106,0 762,0 774,20 94,20" fill="var(--grey-band)"/>
    <polygon points="770,0 868,0 868,20 782,20" fill="var(--teal)"/>
  </svg>

  <div class="discount">
    <div class="discount__label">use discount code<br>A012345 &amp; Get</div>
    <div class="discount__amount">5%<small>off</small></div>
  </div>

  <div class="brand">
    <div class="brand__name">VELOSTRIX</div>
    <div class="brand__tagline">think. learn. grow.</div>
  </div>

  <section class="intro">
    <h1 class="section-title">Velostrix's Brain Booster</h1>
    <p>Velostrix Brain Booster is a natural cognitive enhancement supplement. It is scientifically formulated to increase your brain's abilities to learn, to remember, to focus and to get things done. In clinical terms, it is a nootropic.</p>
    <p>This is a term that came from Greek, where noos means ‘mind’ and trope means ‘turning’. Nootropics transform the brain so that it works harder and smarter. For this reason, they are sometimes referred to in the press as smart drugs, intelligence enhancers and memory enhancers.</p>
    <p>If learning and remembering is important—if you want better concentration and a heightened ability to get things done—then give Velostrix a try.</p>
  </section>

  <section class="benefits">
    <h2 class="section-title">Benefits of<br>Velostrix's Brain Booster</h2>
    <ul class="benefit-list">
      <li><svg viewBox="0 0 18 18"><path d="M2 9.5l4.5 4.5L16 4" fill="none" stroke="var(--teal)" stroke-width="3"/></svg>Stronger Memory</li>
      <li><svg viewBox="0 0 18 18"><path d="M2 9.5l4.5 4.5L16 4" fill="none" stroke="var(--teal)" stroke-width="3"/></svg>Sharper Focus</li>
      <li><svg viewBox="0 0 18 18"><path d="M2 9.5l4.5 4.5L16 4" fill="none" stroke="var(--teal)" stroke-width="3"/></svg>Better Cognition</li>
      <li><svg viewBox="0 0 18 18"><path d="M2 9.5l4.5 4.5L16 4" fill="none" stroke="var(--teal)" stroke-width="3"/></svg>Greater Mental Energy</li>
      <li><svg viewBox="0 0 18 18"><path d="M2 9.5l4.5 4.5L16 4" fill="none" stroke="var(--teal)" stroke-width="3"/></svg>Higher Productivity</li>
    </ul>
  </section>

  <svg class="guarantee-seal" viewBox="0 0 156 156" aria-hidden="true">
    <circle cx="78" cy="78" r="74" fill="var(--teal)"/>
  </svg>

  <div class="product-photo" role="img" aria-label="Photo of a white supplement bottle with a teal label"></div>

  <div class="owl-photo" role="img" aria-label="Photo of an owl flying towards the viewer with wings spread wide"></div>

  <address class="contact contact--address">
    <div class="contact__row">
      <svg viewBox="0 0 16 16"><path d="M8 1a5 5 0 0 0-5 5c0 4 5 9 5 9s5-5 5-9a5 5 0 0 0-5-5zm0 7a2 2 0 1 1 0-4 2 2 0 0 1 0 4z" fill="var(--teal)"/></svg>
      <span>Suite 48, 212 Harbour Rd,</span>
    </div>
    <div class="contact__indent">Brisbane, 4000, Australia</div>
  </address>

  <address class="contact contact--online">
    <div class="contact__row">
      <svg viewBox="0 0 16 16"><rect x="1" y="3" width="14" height="10" fill="var(--teal)"/><path d="M1 3l7 6 7-6" fill="none" stroke="#fff" stroke-width="1.4"/></svg>
      <span>support@velostrix.com</span>
    </div>
    <div class="contact__row">
      <svg viewBox="0 0 16 16"><circle cx="8" cy="8" r="6.5" fill="none" stroke="var(--teal)" stroke-width="1.5"/><ellipse cx="8" cy="8" rx="3" ry="6.5" fill="none" stroke="var(--teal)" stroke-width="1.2"/><path d="M1.5 8h13" stroke="var(--teal)" stroke-width="1.2"/></svg>
      <span>www.velostrix.com</span>
    </div>
  </address>

  <svg class="edge-band edge-band--bottom" viewBox="0 0 868 20" preserveAspectRatio="none">
    <polygon points="0,0 86,0 98,20 0,20" fill="var(--teal)"/>
    <polygon points="94,0 774,0 762,20 106,20" fill="var(--grey-band)"/>
    <polygon points="782,0 868,0 868,20 770,20" fill="var(--teal)"/>
  </svg>
</main>
</body>
</html>
```